Larvik Consulting

Hi,
I have my own network consulting business (just me)
and need to get a logo and business card design together,

Based in New Zealand,

Tobias Wrenfield
Unified Communications and Network Architect

/design engineer,
and would like this to be the basis for personal branding and company identity

Industry/Entity Type

Business

Requirements
Nice to have
• I have the basis for a optional logo - needs color -

```html
<!DOCTYPE html>
<html lang="en">
<head>
<meta charset="utf-8">
<title>Larvik Consulting – Business Card</title>
<link href="https://fonts.googleapis.com/css2?family=Exo+2:ital,wght@0,400;1,400;1,600;1,700&display=swap" rel="stylesheet">
<style>
  :root {
    --page: #ffffff;
    --card-center: #f4feff;
    --card-edge: #c9fbfd;
    --brand-blue: #1e8fe0;
    --accent-cyan: #00c8f5;
    --rule-cyan: #19e6f2;
    --ink: #0a0a0a;
    --mark-fill: #b6f4fa;
  }
  html, body {
    margin: 0;
    padding: 0;
    width: 1200px;
    height: 960px;
    overflow: hidden;
    background: var(--page);
    font-family: "Exo 2", sans-serif;
  }
  .canvas {
    position: relative;
    width: 1200px;
    height: 960px;
  }
  .card {
    position: absolute;
    left: 258px;
    width: 691px;
    height: 395px;
    border-radius: 40px;
    overflow: hidden;
    background: radial-gradient(ellipse at 50% 45%, var(--card-center) 0%, #e2fdfe 45%, var(--card-edge) 100%);
  }
  .card--front { top: 66px; }
  .card--back { top: 500px; }

  .wordmark {
    position: absolute;
    margin: 0;
    color: var(--brand-blue);
    font-weight: 400;
    white-space: nowrap;
    letter-spacing: 0.2px;
  }
  .card--front .wordmark {
    left: 21px;
    top: 103px;
    font-size: 20px;
  }
  .card--front .brand-dot {
    position: absolute;
    left: 82px;
    top: 28px;
    width: 62px;
    height: 62px;
    border-radius: 50%;
    background: var(--mark-fill);
  }

  .holder {
    position: absolute;
    left: 0;
    width: 691px;
    top: 178px;
    text-align: center;
  }
  .holder__name {
    display: inline-block;
    margin: 0;
    font-size: 25px;
    font-style: italic;
    font-weight: 700;
    color: var(--ink);
    padding: 0 16px 1px;
    border-bottom: 3px solid var(--rule-cyan);
    letter-spacing: 0.5px;
  }
  .holder__title {
    margin: 5px 0 0;
    font-size: 13px;
    font-style: italic;
    font-weight: 400;
    color: var(--ink);
  }

  .accent-band {
    position: absolute;
    left: 0;
    top: 332px;
    width: 415px;
    height: 12px;
    background: var(--accent-cyan);
  }

  .contact {
    position: absolute;
    left: 45px;
    top: 351px;
    margin: 0;
    padding: 0;
    list-style: none;
  }
  .contact__item {
    display: flex;
    align-items: center;
    height: 21px;
    font-size: 11px;
    font-style: italic;
    letter-spacing: 5px;
    color: var(--ink);
  }
  .contact__icon {
    width: 17px;
    height: 17px;
    margin-right: 13px;
    flex: none;
  }

  .card--back .brand-dot {
    position: absolute;
    left: 307px;
    top: 125px;
    width: 90px;
    height: 90px;
    border-radius: 50%;
    background: var(--mark-fill);
  }
  .card--back .wordmark {
    left: 0;
    width: 691px;
    text-align: center;
    top: 252px;
    font-size: 31px;
  }
  .website {
    position: absolute;
    left: 0;
    width: 691px;
    top: 362px;
    margin: 0;
    text-align: center;
    font-size: 15px;
    font-style: italic;
    font-weight: 600;
    color: var(--brand-blue);
  }
</style>
</head>
<body>
<main class="canvas">
  <section class="card card--front" aria-label="Business card front">
    <span class="brand-dot" aria-hidden="true"></span>
    <p class="wordmark">larvik consulting</p>

    <div class="holder">
      <h1 class="holder__name">Tobias Wrenfield</h1>
      <p class="holder__title">Unified Communications and Network Architect</p>
    </div>

    <div class="accent-band" aria-hidden="true"></div>

    <ul class="contact">
      <li class="contact__item">
        <svg class="contact__icon" viewBox="0 0 20 20" aria-hidden="true">
          <circle cx="10" cy="10" r="9" fill="none" stroke="#0a0a0a" stroke-width="1.3"/>
          <path d="M6.6 5.2c.5-.4 1.1-.3 1.4.2l.9 1.5c.3.5.1 1-.3 1.3l-.6.4c.5 1.3 1.5 2.3 2.8 2.9l.5-.6c.3-.4.9-.5 1.3-.2l1.5.9c.5.3.6.9.2 1.4l-.6.7c-.5.5-1.3.7-2 .4-2.7-1-4.8-3.2-5.8-5.9-.2-.7 0-1.5.5-2z" fill="none" stroke="#0a0a0a" stroke-width="1.1"/>
        </svg>
        <span>0 210 555 048</span>
      </li>
      <li class="contact__item">
        <svg class="contact__icon" viewBox="0 0 20 20" aria-hidden="true">
          <circle cx="10" cy="10" r="9" fill="none" stroke="#0a0a0a" stroke-width="1.3"/>
          <rect x="5.2" y="6.7" width="9.6" height="6.6" fill="none" stroke="#0a0a0a" stroke-width="1.1"/>
          <path d="M5.2 6.7l4.8 3.8 4.8-3.8" fill="none" stroke="#0a0a0a" stroke-width="1.1"/>
        </svg>
        <span>tobias@wrenfield.com</span>
      </li>
    </ul>
  </section>

  <section class="card card--back" aria-label="Business card back">
    <span class="brand-dot" aria-hidden="true"></span>
    <p class="wordmark">larvik consulting</p>
    <p class="website">www.larvikconsulting.com</p>
  </section>
</main>
</body>
</html>
```